Simon Ashgrove Pianist Teacher Examiner

I need a website design to promote my business as a professional classical pianist and a piano teacher of all levels.
I want it to look a mixture of old world opulence (eg antique grand piano?) and modern text. It should have an elegant, beautiful and relaxing feel.

Industry/Entity Type

Teacher

```html
<!DOCTYPE html>
<html lang="en">
<head>
<meta charset="utf-8">
<title>Simon Ashgrove — Classical Pianist</title>
<link href="https://fonts.googleapis.com/css2?family=Anton&family=Oswald:wght@500;700&family=Arimo:wght@400&display=swap" rel="stylesheet">
<style>
  :root {
    --ink: #111111;
    --white: #ffffff;
    --hero-dark: #2b2b2d;
    --hero-mid: #3d3d40;
    --hero-grey: #7a7a7a;
    --hero-deep: #1e1e1e;
    --footer: #3a3a3a;
    --footer-text: #bdbdbd;
    --arrow-box: #6e6e6e;
    --body-text: #333333;
  }
  * { margin: 0; padding: 0; box-sizing: border-box; }
  html, body { width: 734px; height: 1200px; overflow: hidden; background: var(--white); }
  body { position: relative; font-family: "Arimo", Arial, sans-serif; color: var(--body-text); }

  .hero { position: absolute; left: 0; top: 0; width: 734px; height: 455px; }
  .hero-photo {
    position: absolute; inset: 0;
    background: radial-gradient(ellipse 200px 260px at 360px 250px, #6b625c 0%, #4a4444 45%, transparent 75%),
                linear-gradient(180deg, var(--hero-mid) 0%, var(--hero-dark) 70%, #1c1c1d 100%);
  }
  .brand {
    position: absolute; left: 105px; top: 20px;
    font-family: "Oswald", sans-serif; font-weight: 700; font-size: 25px;
    color: var(--white); letter-spacing: -0.3px;
  }
  .main-nav { position: absolute; top: 31px; left: 0; width: 734px; }
  .main-nav a {
    position: absolute; font-family: "Oswald", sans-serif; font-weight: 700;
    font-size: 10px; color: var(--white); text-decoration: none; white-space: nowrap;
  }
  .hero-title {
    position: absolute; left: 488px; top: 210px;
    font-family: "Anton", sans-serif; font-size: 25px; line-height: 30px; letter-spacing: 0.2px;
  }
  .hero-title .line-a { color: var(--hero-grey); display: block; }
  .hero-title .line-b { color: var(--hero-deep); display: block; }
  .hero-arrows { position: absolute; left: 647px; top: 290px; }

  .intro-title, .gallery-title, .about-text, .intro-text {
    position: absolute; left: 0; width: 734px; text-align: center;
  }
  .intro-title, .gallery-title { font-family: "Anton", sans-serif; color: var(--ink); font-weight: 400; }
  .intro-title { top: 486px; font-size: 26px; }
  .intro-text, .about-text {
    font-size: 7px; line-height: 14px; padding: 0 126px;
  }
  .intro-text { top: 530px; }

  .about-badge {
    position: absolute; left: 309px; top: 602px; width: 114px; height: 114px;
    border-radius: 50%; background: var(--ink); color: var(--white);
    display: flex; flex-direction: column; align-items: center; justify-content: center;
    font-family: "Oswald", sans-serif; font-weight: 700;
  }
  .about-badge .badge-title { font-size: 16px; line-height: 19px; }
  .about-badge .badge-name { font-size: 12px; line-height: 16px; }
  .about-text { top: 735px; }
  .read-more {
    position: absolute; left: 304px; top: 793px; width: 126px; height: 29px;
    background: var(--ink); color: var(--white); text-decoration: none;
    font-family: "Oswald", sans-serif; font-weight: 700; font-size: 9px;
    display: flex; align-items: center; justify-content: center;
  }

  .gallery-title { top: 844px; font-size: 26px; }
  .gallery-arrows { position: absolute; left: 605px; top: 864px; display: flex; gap: 1px; }
  .gallery-arrows span { width: 12px; height: 11px; background: var(--arrow-box); display: block; }
  .gallery { position: absolute; left: 105px; top: 897px; width: 525px; height: 206px; display: flex; gap: 1px; }
  .gallery .shot { flex: 1; height: 100%; }
  .shot-suit { background: linear-gradient(160deg, #bdb8b2 0%, #5a5860 45%, #26262c 100%); }
  .shot-hall { background: linear-gradient(180deg, #4e4535 0%, #7b6c52 45%, #2f2a22 100%); }
  .shot-portrait { background: radial-gradient(ellipse 50px 60px at 50% 35%, #7a6e66 0%, #3a3838 70%), #333333; }

  .site-footer { position: absolute; left: 0; top: 1134px; width: 734px; height: 66px; background: var(--footer); }
  .footer-nav { position: absolute; left: 105px; top: 18px; font-family: "Oswald", sans-serif; font-size: 6px; font-weight: 500; color: var(--footer-text); white-space: nowrap; }
  .footer-nav a { color: var(--footer-text); text-decoration: none; }
  .footer-nav .sep { margin: 0 10px; }
  .copyright { position: absolute; left: 105px; top: 35px; font-family: "Oswald", sans-serif; font-size: 6px; color: var(--footer-text); }
  .follow { position: absolute; left: 494px; top: 24px; display: flex; align-items: center; gap: 5px; font-family: "Oswald", sans-serif; font-size: 6px; color: var(--footer-text); }
  .follow .dot { width: 12px; height: 12px; border-radius: 50%; background: #8a8a8a; display: block; }
  .follow .label { margin-right: 3px; }
</style>
</head>
<body>
  <header class="hero">
    <div class="hero-photo" role="img" aria-label="Portrait of the pianist in a dark leather jacket against a dark grey wall"></div>
    <div class="brand">Simon Ashgrove</div>
    <nav class="main-nav">
      <a href="#" style="left:402px">HOME</a>
      <a href="#" style="left:455px">ABOUT ME</a>
      <a href="#" style="left:524px">LEVELS</a>
      <a href="#" style="left:580px">CONTACT US</a>
    </nav>
    <h2 class="hero-title"><span class="line-a">My professional is</span><span class="line-b">classical pianist</span></h2>
    <svg class="hero-arrows" width="42" height="22" viewBox="0 0 42 22" aria-hidden="true">
      <polyline points="11,2 3,11 11,20" fill="none" stroke="#8a8a8a" stroke-width="1.2"/>
      <polyline points="31,2 39,11 31,20" fill="none" stroke="#8a8a8a" stroke-width="1.2"/>
    </svg>
  </header>

  <h1 class="intro-title">My professional is classical pianist</h1>
  <p class="intro-text">It is a long established fact that a reader will be distracted by the readable content of a page when looking at its layout. The point of using Lorem Ipsum is that it has a more-or-less normal distribution of letters, as opposed to using 'Content here, content here', making it look like readable English. Many desktop publishing packages and web page editors now use Lorem Ipsum as their default model text, and a search...</p>

  <div class="about-badge"><span class="badge-title">About Me</span><span class="badge-name">Simon Ashgrove</span></div>
  <p class="about-text">It is a long established fact that a reader will be distracted by the readable content of a page when looking at its layout. The point of using Lorem Ipsum is that it has a more-or-less normal distribution of letters, as opposed to using 'Content here, content here', making it look like readable English. Many desktop publishing packages and web page editors now use Lorem Ipsum as their default model text, and a search...</p>
  <a class="read-more" href="#">READ MORE ABOUT ME</a>

  <h2 class="gallery-title">Photo Gallery</h2>
  <div class="gallery-arrows" aria-hidden="true">
    <span><svg width="12" height="11" viewBox="0 0 12 11"><polyline points="7,3 4.5,5.5 7,8" fill="none" stroke="#fff" stroke-width="0.9"/></svg></span>
    <span><svg width="12" height="11" viewBox="0 0 12 11"><polyline points="5,3 7.5,5.5 5,8" fill="none" stroke="#fff" stroke-width="0.9"/></svg></span>
  </div>
  <div class="gallery">
    <div class="shot shot-suit" role="img" aria-label="Seated man in a dark suit and patterned tie"></div>
    <div class="shot shot-hall" role="img" aria-label="Antique grand piano in an ornate gilded hall"></div>
    <div class="shot shot-portrait" role="img" aria-label="Portrait of the pianist against a dark wall"></div>
  </div>

  <footer class="site-footer">
    <nav class="footer-nav"><a href="#">HOME</a><span class="sep">I</span><a href="#">ABOUT ME</a><span class="sep">I</span><a href="#">LEVELS</a><span class="sep">I</span><a href="#">CONTACT US</a></nav>
    <p class="copyright">© COPYRIGHT 2014. SIMON ASHGROVE. ALL RIGHTS RESERVED.</p>
    <div class="follow"><span class="label">FOLLOW US :</span><span class="dot"></span><span class="dot"></span><span class="dot"></span><span class="dot"></span><span class="dot"></span><span class="dot"></span></div>
  </footer>
</body>
</html>
```